Road Construction Company needs business cards

We would like a new business card designed for our business.

We're a road construction company based in Qld, Australia.

Can the business card please have the following information on it.

Name: Brent Malvoy
Position: General Manager
Phone: 0471 592 304
Email: Brent.malvoy@quendix.com.au
Address: 87 Harrowgate Ave, Pindarra, QLD, 4000
Website: www.quendix.com.au

Visually we'd like the card to be professional and simple.

Attached is our logo.

Our website is www.quendix.com.au

Target Market(s)

Men aged 25-60

Contact Information for Business Card

As listed in project description

Font styles to use
Serif

Requirements
Must have
• Large logo on back of card

```html
<!DOCTYPE html>
<html lang="en">
<head>
<meta charset="utf-8">
<title>Quendix Business Card</title>
<link href="https://fonts.googleapis.com/css2?family=Poppins:wght@400;600;700;800&display=swap" rel="stylesheet">
<style>
  :root {
    --backdrop: #959595;
    --card-dark: #231f20;
    --card-light: #f8f8f8;
    --accent: #2ba3d9;
    --brand-blue: #1d5fb0;
    --text-white: #ffffff;
    --text-muted: #8c8c8c;
  }
  html, body {
    margin: 0;
    padding: 0;
    width: 1200px;
    height: 1000px;
    overflow: hidden;
    background: var(--backdrop);
    font-family: "Poppins", sans-serif;
  }
  .stage {
    position: relative;
    width: 1200px;
    height: 1000px;
  }
  .card {
    position: absolute;
    top: 180px;
    width: 351px;
    height: 615px;
    border-radius: 28px;
    box-shadow: 0 2px 6px rgba(0,0,0,0.18);
  }
  .card-front {
    left: 247px;
    background: var(--card-dark);
    text-align: center;
  }
  .card-back {
    left: 657px;
    background: var(--card-light);
  }
  .wordmark {
    position: absolute;
    left: 0;
    right: 0;
    margin: 0;
    text-align: center;
    font-family: "Poppins", sans-serif;
    font-weight: 800;
    font-size: 46px;
    letter-spacing: 2px;
    line-height: 1;
  }
  .card-front .wordmark {
    top: 62px;
    color: var(--text-white);
  }
  .card-back .wordmark {
    top: 284px;
    color: var(--brand-blue);
  }
  .person-name {
    position: absolute;
    top: 341px;
    left: 0;
    right: 0;
    margin: 0;
    color: var(--text-white);
    font-weight: 700;
    font-size: 21px;
    letter-spacing: 1px;
    text-transform: uppercase;
  }
  .person-title {
    position: absolute;
    top: 372px;
    left: 0;
    right: 0;
    margin: 0;
    color: var(--accent);
    font-size: 13px;
    letter-spacing: 1px;
    text-transform: uppercase;
  }
  .address {
    position: absolute;
    top: 405px;
    left: 0;
    right: 0;
    margin: 0;
    color: var(--text-muted);
    font-size: 13.5px;
    line-height: 17px;
    font-style: normal;
  }
  .contact-icons {
    position: absolute;
    top: 468px;
    left: 0;
    right: 0;
    display: flex;
    justify-content: center;
    gap: 8px;
  }
  .contact-icons svg {
    width: 33px;
    height: 33px;
  }
  .contact-list {
    position: absolute;
    top: 514px;
    left: 0;
    right: 0;
    margin: 0;
    padding: 0;
    list-style: none;
    color: var(--text-muted);
    font-size: 16.5px;
    line-height: 19px;
  }
</style>
</head>
<body>
<div class="stage">
  <section class="card card-front">
    <p class="wordmark">QUENDIX</p>
    <h1 class="person-name">Brent Malvoy</h1>
    <p class="person-title">General Manager</p>
    <address class="address">87 Harrowgate Ave,<br>Pindarra, QLD, 4000</address>
    <div class="contact-icons">
      <svg viewBox="0 0 33 33" aria-label="Phone">
        <circle cx="16.5" cy="16.5" r="15.5" fill="none" stroke="var(--accent)" stroke-width="1.2"/>
        <path d="M11 10.5c1-1 2-1 2.6 0l1.3 2c.4.7.2 1.3-.4 1.8l-.8.6c.7 1.6 2 2.9 3.5 3.6l.6-.8c.5-.6 1.1-.8 1.8-.4l2 1.3c1 .6 1 1.6 0 2.6-1 1-2.6 1.4-4.3.5-2.8-1.5-5-3.7-6.5-6.5-.9-1.7-.5-3.3.2-4.7z" fill="var(--accent)"/>
      </svg>
      <svg viewBox="0 0 33 33" aria-label="Email">
        <circle cx="16.5" cy="16.5" r="15.5" fill="none" stroke="var(--accent)" stroke-width="1.2"/>
        <rect x="9.5" y="12" width="14" height="10" fill="var(--accent)"/>
        <path d="M9.5 12l7 5.5 7-5.5" fill="none" stroke="var(--card-dark)" stroke-width="1"/>
      </svg>
      <svg viewBox="0 0 33 33" aria-label="Website">
        <circle cx="16.5" cy="16.5" r="15.5" fill="none" stroke="var(--accent)" stroke-width="1.2"/>
        <g fill="none" stroke="var(--accent)" stroke-width="1.3">
          <circle cx="16.5" cy="16.5" r="7"/>
          <ellipse cx="16.5" cy="16.5" rx="3" ry="7"/>
          <line x1="9.5" y1="16.5" x2="23.5" y2="16.5"/>
          <line x1="10.5" y1="13" x2="22.5" y2="13"/>
          <line x1="10.5" y1="20" x2="22.5" y2="20"/>
        </g>
      </svg>
    </div>
    <ul class="contact-list">
      <li>0471 592 304</li>
      <li>brent.malvoy@quendix.com.au</li>
      <li>quendix.com.au</li>
    </ul>
  </section>
  <section class="card card-back">
    <p class="wordmark">QUENDIX</p>
  </section>
</div>
</body>
</html>
```